Referral card and Flyer design

Please see attached example of Flyer and Referral Card. I would like a similar type flyer and card but nicer design. Industrial/retro Automtive type design.

Referral card should be size of regular business card.

Flyer should be 8X10" typical printer paper size.

Business Logo and Name should be changed from Vantorel to GearHollow LLC and on flyer please remove the last option where it says ( a Night out on us ) .

Change address on referral card to
GearHollow LLC
412 N Pellam Rd
Youngsville NC 27583
GearHollowHaul.example
Call or Text 919-555-0147

```html
<!DOCTYPE html>
<html lang="en">
<head>
<meta charset="utf-8">
<title>GearHollow LLC – Customer Referral Flyer and Card</title>
<link href="https://fonts.googleapis.com/css2?family=Montserrat:wght@300;400;500;600;700;800;900&family=Oswald:wght@500;600&display=swap" rel="stylesheet">
<style>
  :root{
    --navy:#283593;
    --navy-deep:#1f2a7a;
    --ink:#1e1e1e;
    --text:#2b2b2b;
    --grey:#8a8a8a;
    --silver:#c9ccd4;
    --paper:#ffffff;
    --stage:#ececec;
  }
  *{margin:0;padding:0;box-sizing:border-box}
  html,body{width:1200px;height:2944px;overflow:hidden}
  body{background:var(--stage);font-family:"Montserrat",sans-serif;color:var(--text);position:relative}

  /* ---------- Flyer ---------- */
  .flyer{position:absolute;left:181px;top:654px;width:837px;height:1046px;background:var(--paper);overflow:hidden;box-shadow:0 10px 30px rgba(0,0,0,.25)}
  .flyer-header{position:absolute;left:0;top:0}
  .brand{position:absolute;display:flex;align-items:center;gap:10px;font-weight:800;letter-spacing:.5px}
  .flyer .brand{left:70px;top:74px;color:var(--navy);font-size:28px}
  .brand-dot{width:20px;height:20px;border-radius:50%;background:currentColor}
  .flyer-title{position:absolute;left:44px;top:182px;color:#fff;line-height:1}
  .flyer-title .light{display:block;font-weight:400;font-size:52px;letter-spacing:1px}
  .flyer-title .bold{display:block;font-weight:800;font-size:60px;margin-top:4px;letter-spacing:.5px}
  .section-head{position:absolute;left:45px;font-weight:700;font-size:26px;color:var(--navy)}
  .section-head .dark{color:var(--ink)}
  .about-head{top:373px}
  .about-copy{position:absolute;left:45px;top:412px;width:700px;font-size:14.5px;line-height:1.22;color:var(--text)}
  .easy-head{top:478px}
  .step{position:absolute;display:flex;gap:10px;font-weight:600;font-size:20px;color:var(--ink);line-height:1.22}
  .step-num{flex:none;width:28px;height:28px;border-radius:50%;background:var(--navy);color:#fff;font-size:16px;font-weight:700;display:flex;align-items:center;justify-content:center;margin-top:-1px;box-shadow:0 0 0 2px #fff,0 0 0 3px var(--navy)}
  .step-1{left:53px;top:523px}
  .step-2{left:53px;top:567px}
  .step-3{left:400px;top:567px}
  .ticks{position:absolute;list-style:none;font-size:16px;font-weight:500;color:var(--ink)}
  .ticks li{display:flex;align-items:center;gap:10px;height:24px}
  .ticks svg{width:12px;height:12px;flex:none}
  .ticks-2{left:93px;top:600px}
  .ticks-3{left:438px;top:643px}
  .ticks-3 li{height:32px}
  .present-note{position:absolute;left:46px;top:681px;font-size:15px;font-weight:500;line-height:1.15;color:var(--ink)}
  .cta{position:absolute;left:0;width:100%;top:733px;text-align:center;font-weight:600;font-size:22px;letter-spacing:.5px;color:var(--navy)}
  .photo{position:absolute;top:783px;width:227px;height:135px;border:4px solid #fff;box-shadow:0 2px 8px rgba(0,0,0,.35)}
  .photo-fuel{left:46px;background:linear-gradient(100deg,#b2262a 0%,#7f8590 45%,#3d6b3f 70%,#d8d8d8 100%)}
  .photo-cash{left:304px;background:linear-gradient(135deg,#b9bfae,#7d8873 50%,#c8cbbb)}
  .photo-dinner{left:561px;background:linear-gradient(120deg,#2d3a52,#6b6f78 50%,#c9c4bd)}
  .footer-dark{position:absolute;left:0;top:945px;width:472px;height:84px;background:var(--ink);clip-path:polygon(0 0,455px 0,472px 100%,0 100%);color:#fff;padding:8px 0 0 53px}
  .footer-dark .call{font-weight:700;font-size:23px;letter-spacing:.5px}
  .footer-dark .addr{display:flex;align-items:center;gap:6px;font-weight:600;font-size:16px;margin-top:5px}
  .footer-blue{position:absolute;left:458px;top:957px;width:379px;height:58px;background:var(--navy);clip-path:polygon(0 0,100% 0,100% 100%,14px 100%);color:#fff;padding:6px 0 0 32px;font-weight:600;font-size:16px;line-height:1.5}
  .footer-blue div{display:flex;align-items:center;gap:10px}
  .footer svg,.footer-blue svg,.footer-dark svg{flex:none}

  /* ---------- Referral card ---------- */
  .card{position:absolute;left:181px;top:1810px;width:839px;height:480px;background:var(--paper);overflow:hidden;box-shadow:0 10px 30px rgba(0,0,0,.25)}
  .card-bands{position:absolute;left:0;top:0}
  .card .brand{left:76px;top:92px;color:#fff;font-size:28px}
  .card-title{position:absolute;left:372px;top:36px;line-height:1}
  .card-title .big{display:block;font-weight:900;font-size:64px;color:var(--silver);letter-spacing:1px}
  .card-title .sub{display:block;font-weight:800;font-size:47px;color:#fff;margin-top:4px}
  .card-lead{position:absolute;left:45px;top:238px;font-weight:700;font-size:22px;line-height:1.25;color:var(--ink)}
  .offer{position:absolute;left:469px;top:200px;width:273px;height:82px;border-radius:16px;background:var(--ink);color:#fff;font-family:"Oswald",sans-serif;font-weight:600;font-size:60px;line-height:82px;text-align:center;letter-spacing:-1px}
  .offer sup{font-size:28px;vertical-align:top;line-height:46px;margin-right:2px}
  .referred{position:absolute;left:45px;top:296px;font-weight:700;font-size:24px;color:var(--navy)}
  .fill-line{position:absolute;height:1px;background:#555}
  .fill-line-1{left:246px;top:324px;width:562px}
  .fill-line-2{left:46px;top:370px;width:762px}
  .card-contact{position:absolute;left:45px;top:405px;display:flex;align-items:center;font-weight:600;font-size:19px;color:var(--ink);white-space:nowrap}
  .card-contact .gap{display:inline-block;width:24px}
  .card-contact svg{margin-right:8px}
</style>
</head>
<body>

<article class="flyer">
  <svg class="flyer-header" width="837" height="420" viewBox="0 0 837 420" aria-hidden="true">
    <defs>
      <linearGradient id="carScene" x1="0" y1="0" x2="0" y2="1">
        <stop offset="0" stop-color="#5f6a3e"/>
        <stop offset=".45" stop-color="#8b8f6c"/>
        <stop offset=".6" stop-color="#b3262a"/>
        <stop offset=".8" stop-color="#6e6f72"/>
        <stop offset="1" stop-color="#9a9b9d"/>
      </linearGradient>
    </defs>
    <rect x="0" y="169" width="837" height="193" fill="var(--navy)"/>
    <circle cx="712" cy="34" r="380" fill="none" stroke="var(--navy)" stroke-width="12"/>
    <circle cx="712" cy="34" r="366" fill="#fff" stroke="#6d6d6d" stroke-width="8"/>
    <circle cx="712" cy="34" r="356" fill="url(#carScene)"/>
  </svg>
  <div role="img" aria-label="Photo of a red sports coupe driving along a road in front of trees" style="position:absolute;left:370px;top:0;width:467px;height:390px"></div>

  <div class="brand"><span class="brand-dot"></span>GearHollow LLC</div>

  <h1 class="flyer-title">
    <span class="light">CUSTOMER</span>
    <span class="bold">REFERRAL<br>PROGRAM</span>
  </h1>

  <h2 class="section-head about-head">ABOUT <span class="dark">US</span></h2>
  <p class="about-copy">If you are in the market for a dependable pre-owned vehicle, I encourage you to come see us at GearHollow LLC. We have cars, trucks, and suvs in almost every year, make, model, at pricing you can afford. To save big on your next car, you have definitely come to the right place!</p>

  <h2 class="section-head easy-head">EASY AS 1..2..3!</h2>

  <div class="step step-1"><span class="step-num">1</span><span>Wegive you tv Referral Cards with your name anthem</span></div>
  <div class="step step-2"><span class="step-num">2</span><span>Give the cardstoa</span></div>
  <ul class="ticks ticks-2">
    <li><svg viewBox="0 0 12 12"><circle cx="6" cy="6" r="6" fill="var(--navy)"/><path d="M3.2 6.2l1.9 1.8 3.7-3.9" stroke="#fff" stroke-width="1.6" fill="none"/></svg>Family member</li>
    <li><svg viewBox="0 0 12 12"><circle cx="6" cy="6" r="6" fill="var(--navy)"/><path d="M3.2 6.2l1.9 1.8 3.7-3.9" stroke="#fff" stroke-width="1.6" fill="none"/></svg>Friend</li>
    <li><svg viewBox="0 0 12 12"><circle cx="6" cy="6" r="6" fill="var(--navy)"/><path d="M3.2 6.2l1.9 1.8 3.7-3.9" stroke="#fff" stroke-width="1.6" fill="none"/></svg>Co-worker</li>
  </ul>
  <div class="step step-3"><span class="step-num">3</span><span>When acard isredeemed, as a<br>thank you, you can choose either:</span></div>
  <ul class="ticks ticks-3">
    <li><svg viewBox="0 0 12 12"><circle cx="6" cy="6" r="6" fill="var(--navy)"/><path d="M3.2 6.2l1.9 1.8 3.7-3.9" stroke="#fff" stroke-width="1.6" fill="none"/></svg>525.00 Fuel Card</li>
    <li><svg viewBox="0 0 12 12"><circle cx="6" cy="6" r="6" fill="var(--navy)"/><path d="M3.2 6.2l1.9 1.8 3.7-3.9" stroke="#fff" stroke-width="1.6" fill="none"/></svg>525.00 Credit for repairs</li>
  </ul>
  <p class="present-note">They present the card &amp; save 525.00 an<br>ary service —f'a Srnngs Attacned!</p>

  <p class="cta">ASK FOR YOUR CARDS TODAY!</p>

  <div class="photo photo-fuel" role="img" aria-label="Photo of a fuel nozzle filling a red car"></div>
  <div class="photo photo-cash" role="img" aria-label="Photo of a pile of banknotes"></div>
  <div class="photo photo-dinner" role="img" aria-label="Photo of a couple toasting at a restaurant table"></div>

  <div class="footer-dark">
    <div class="call">CALL OR TEXT 919-555-0147</div>
    <div class="addr"><svg width="12" height="16" viewBox="0 0 12 16"><path d="M6 0a6 6 0 0 0-6 6c0 4.5 6 10 6 10s6-5.5 6-10a6 6 0 0 0-6-6z" fill="#fff"/><circle cx="6" cy="6" r="2.2" fill="var(--ink)"/></svg>412 N Pellam Rd Youngsville NC 27583</div>
  </div>
  <div class="footer-blue">
    <div><svg width="15" height="15" viewBox="0 0 16 16"><rect x="1" y="3" width="14" height="10" rx="1.5" fill="none" stroke="#fff" stroke-width="1.6"/><path d="M1.5 4l6.5 5 6.5-5" fill="none" stroke="#fff" stroke-width="1.6"/></svg>sales@gearhollowhaul.example</div>
    <div><svg width="15" height="15" viewBox="0 0 16 16"><circle cx="8" cy="8" r="6.8" fill="none" stroke="#fff" stroke-width="1.4"/><ellipse cx="8" cy="8" rx="3" ry="6.8" fill="none" stroke="#fff" stroke-width="1.2"/><path d="M1.2 8h13.6" stroke="#fff" stroke-width="1.2"/></svg>www.gearhollowhaul.example</div>
  </div>
</article>

<article class="card">
  <svg class="card-bands" width="839" height="480" viewBox="0 0 839 480" aria-hidden="true">
    <polygon points="0,0 839,0 839,163 414,163 394,187 0,187" fill="var(--navy)"/>
    <polygon points="0,187 394,187 414,163 839,163 839,174 420,174 400,198 0,198" fill="#fff"/>
    <polygon points="0,189 398,189 418,165 839,165 839,172 421,172 401,196 0,196" fill="var(--ink)"/>
    <polygon points="0,450 520,450 530,480 0,480" fill="var(--ink)"/>
    <polygon points="528,462 839,462 839,480 536,480" fill="var(--navy)"/>
  </svg>
  <div class="brand"><span class="brand-dot"></span>GearHollow LLC</div>
  <h1 class="card-title">
    <span class="big">CUSTOMER</span>
    <span class="sub">REFERRAL CARD</span>
  </h1>
  <p class="card-lead">PRESENT THIS CARD TO RECEIVE<br>YOUR FIRST VISIT WITH US.</p>
  <div class="offer"><sup>$</sup>25.00 OFF</div>
  <p class="referred">REFERRED BY:</p>
  <span class="fill-line fill-line-1"></span>
  <span class="fill-line fill-line-2"></span>
  <div class="card-contact">
    CALL OR TEXT<span class="gap"></span>
    <svg width="18" height="18" viewBox="0 0 18 18"><path d="M4 1.5l3 3-1.8 2.2c.9 2 2.4 3.5 4.4 4.4l2.2-1.8 3 3-2 2.4C8.3 14.5 3.5 9.7 1.6 3.5z" fill="var(--navy)"/></svg>919-555-0147<span class="gap"></span>
    <svg width="14" height="19" viewBox="0 0 12 16"><path d="M6 0a6 6 0 0 0-6 6c0 4.5 6 10 6 10s6-5.5 6-10a6 6 0 0 0-6-6z" fill="var(--navy)"/><circle cx="6" cy="6" r="2.2" fill="#fff"/></svg>412 N Pellam Rd Youngsville NC 27583
  </div>
</article>

</body>
</html>
```